Independence Day Graphics for Sale

I want to create 10 social media graphics (new Pixtaloo size 4:5 (1080 x 1350 pixels) focusing on our July 4th Sale Graphics, using any of the pics attached. Use the attached pics, NO RANDOM STOCK PHOTOGRAPHY. For the color scheme of the graphics, they should all be complementary to the product colors in the photos.
You can add any of the photos attached but none are required. You can do some of the graphics in all text. I mainly need BOLD text that says one of the headlines (10 total) SEE ATTACHED WORD DOCUMENT for the headlines to use.

Target Market(s)

women looking to lose weight

Requirements
Must have
• pics attached and text attached

```html
<!DOCTYPE html>
<html lang="en">
<head>
<meta charset="utf-8">
<title>Don't Wait – Sale Ends Soon</title>
<link rel="stylesheet" href="https://fonts.googleapis.com/css2?family=Montserrat:wght@800&family=Archivo+Black&display=swap">
<style>
  :root {
    --sale-red: #ff3131;
    --band-black: #000000;
    --blush-pink: #f7d0dc;
    --paper-white: #ffffff;
    --deal-green: #2d5249;
  }
  html, body {
    margin: 0;
    padding: 0;
    width: 960px;
    height: 1200px;
    overflow: hidden;
    background: var(--sale-red);
  }
  .sale-poster {
    display: block;
    width: 960px;
    height: 1200px;
  }
  .headline {
    font-family: "Montserrat", sans-serif;
    font-weight: 800;
    fill: var(--paper-white);
  }
  .ends-soon {
    font-family: "Montserrat", sans-serif;
    font-weight: 800;
    fill: var(--paper-white);
  }
  .deal-text {
    font-family: "Archivo Black", sans-serif;
    fill: var(--deal-green);
  }
</style>
</head>
<body>
<svg class="sale-poster" viewBox="0 0 960 1200" xmlns="http://www.w3.org/2000/svg">
  <defs>
    <linearGradient id="model-tones" x1="0" y1="0" x2="0" y2="1">
      <stop offset="0" stop-color="#3a2a24"/>
      <stop offset="0.3" stop-color="#ece8e6"/>
      <stop offset="0.6" stop-color="#e6ddd8"/>
      <stop offset="0.75" stop-color="#1a1a1a"/>
      <stop offset="1" stop-color="#141414"/>
    </linearGradient>
    <linearGradient id="counter-tones" x1="0" y1="0" x2="1" y2="0">
      <stop offset="0" stop-color="#e9e3dc"/>
      <stop offset="1" stop-color="#ddd6cf"/>
    </linearGradient>
  </defs>

  <rect class="background" width="960" height="1200" fill="var(--sale-red)"/>

  <polygon class="accent-band" points="0,948 960,984 960,1078 0,1034" fill="var(--blush-pink)"/>

  <text class="headline" x="140" y="231" font-size="236" textLength="701" lengthAdjust="spacingAndGlyphs">DON’T</text>
  <text class="headline" x="156" y="415" font-size="236" textLength="636" lengthAdjust="spacingAndGlyphs">WAIT!</text>

  <polygon class="banner-band" points="0,445 960,415 960,566 0,597" fill="var(--band-black)"/>
  <text class="ends-soon" x="486" y="543" font-size="104" text-anchor="middle" textLength="558" lengthAdjust="spacingAndGlyphs" transform="rotate(-1.8 486 507)">ENDS SOON</text>

  <g role="img" aria-label="Photo of a smiling woman in a white cropped sweater pointing down at three supplement bottles on a marble counter">
    <rect x="323" y="551" width="305" height="563" rx="40" fill="url(#model-tones)"/>
    <rect x="0" y="1114" width="960" height="86" fill="url(#counter-tones)"/>
    <rect x="370" y="1055" width="160" height="95" rx="8" fill="#f4f2f4"/>
  </g>

  <g class="deal-badge" fill="var(--paper-white)">
    <circle cx="726" cy="788" r="150"/>
    <circle cx="866" cy="788" r="38"/>
    <circle cx="847" cy="858" r="38"/>
    <circle cx="796" cy="909" r="38"/>
    <circle cx="726" cy="928" r="38"/>
    <circle cx="656" cy="909" r="38"/>
    <circle cx="605" cy="858" r="38"/>
    <circle cx="586" cy="788" r="38"/>
    <circle cx="605" cy="718" r="38"/>
    <circle cx="656" cy="667" r="38"/>
    <circle cx="726" cy="648" r="38"/>
    <circle cx="796" cy="667" r="38"/>
    <circle cx="847" cy="718" r="38"/>
  </g>
  <g transform="rotate(7 726 788)">
    <text class="deal-text" x="726" y="768" font-size="112" text-anchor="middle" textLength="206" lengthAdjust="spacingAndGlyphs">25%</text>
    <text class="deal-text" x="726" y="876" font-size="128" text-anchor="middle" textLength="206" lengthAdjust="spacingAndGlyphs">OFF</text>
  </g>
</svg>
</body>
</html>
```